Business Card for Maplethorne Elder Keepers

I need a business card design for a very elite and personalized companion care company. We take care of the client at home with respect, dignity, and our full attention. The design should communicate a classic elegance and trust.

/Users/lorafenwick/Downloads/graphwellhub_121488_23943024_3826329_sourcefile

```html
<!DOCTYPE html>
<html lang="en">
<head>
<meta charset="utf-8">
<title>Maplethorne Elder Keepers – Business Card</title>
<link rel="stylesheet" href="https://fonts.googleapis.com/css2?family=Open+Sans:wght@400;600;700&display=swap">
<style>
  :root {
    --navy: #06487a;
    --sky: #35b3e3;
    --paper: #ffffff;
    --ink: #1d1d1f;
    --backdrop: #e6e8eb;
  }
  * { box-sizing: border-box; margin: 0; padding: 0; }
  html, body { width: 1200px; height: 1021px; overflow: hidden; }
  body {
    background: var(--backdrop);
    font-family: "Open Sans", Arial, sans-serif;
    position: relative;
  }
  .card {
    position: absolute;
    left: 250px;
    width: 700px;
    height: 400px;
    overflow: hidden;
    box-shadow: 0 6px 18px rgba(0,0,0,.18);
  }
  /* Back side */
  .card--back {
    top: 70px;
    background: var(--navy);
    display: flex;
    align-items: center;
    justify-content: center;
  }
  .brand {
    display: flex;
    align-items: center;
    gap: 14px;
  }
  .brand__dot {
    width: 22px; height: 22px;
    border-radius: 50%;
    background: var(--sky);
    flex: none;
  }
  .brand__name {
    font-weight: 600;
    letter-spacing: .06em;
    text-transform: uppercase;
    line-height: 1.15;
  }
  .card--back .brand__name { color: var(--paper); font-size: 34px; }
  /* Front side */
  .card--front {
    top: 550px;
    background: var(--paper);
  }
  .front__panel {
    position: absolute; inset: 0;
    width: 100%; height: 100%;
  }
  .card--front .brand {
    position: absolute;
    left: 44px; top: 42px;
  }
  .card--front .brand__name { color: var(--navy); font-size: 25px; }
  .card--front .brand__dot { width: 16px; height: 16px; }
  .contact {
    position: absolute;
    left: 48px; top: 178px;
    color: var(--ink);
    font-size: 17px;
    line-height: 1.45;
  }
  .contact__address { margin-bottom: 10px; }
  .contact__row { display: flex; align-items: center; gap: 9px; }
  .contact__row svg { width: 17px; height: 17px; flex: none; }
  .person {
    position: absolute;
    right: 44px; bottom: 38px;
    text-align: right;
  }
  .person__name {
    color: var(--sky);
    font-weight: 700;
    font-size: 25px;
    letter-spacing: .02em;
  }
  .person__title {
    color: var(--paper);
    font-size: 19px;
    letter-spacing: .04em;
  }
</style>
</head>
<body>

  <section class="card card--back" aria-label="Card back">
    <div class="brand">
      <span class="brand__dot"></span>
      <span class="brand__name">Maplethorne<br>Elder Keepers</span>
    </div>
  </section>

  <section class="card card--front" aria-label="Card front">
    <svg class="front__panel" viewBox="0 0 700 400" preserveAspectRatio="none" aria-hidden="true">
      <path d="M700 0 L470 0 C400 120 520 250 330 320 C270 345 240 370 225 400 L700 400 Z" fill="var(--navy)"/>
    </svg>

    <div class="brand">
      <span class="brand__dot"></span>
      <span class="brand__name">Maplethorne<br>Elder Keepers</span>
    </div>

    <div class="contact">
      <p class="contact__address">418 NW Linden Court<br>Brookvale, FL 34721</p>
      <p class="contact__row">
        <svg viewBox="0 0 16 16"><rect x="4" y="1.5" width="8" height="13" rx="1.5" fill="none" stroke="var(--sky)" stroke-width="1.4"/><line x1="7" y1="12.3" x2="9" y2="12.3" stroke="var(--sky)" stroke-width="1.2"/></svg>
        555-318-4027
      </p>
      <p class="contact__row">
        <svg viewBox="0 0 16 16"><rect x="1.5" y="3.5" width="13" height="9" fill="none" stroke="var(--sky)" stroke-width="1.4"/><path d="M1.5 3.5 L8 9 L14.5 3.5" fill="none" stroke="var(--sky)" stroke-width="1.4"/></svg>
        rowan@maplethorneek.com
      </p>
      <p class="contact__row">
        <svg viewBox="0 0 16 16"><circle cx="8" cy="8" r="6.5" fill="none" stroke="var(--sky)" stroke-width="1.4"/><ellipse cx="8" cy="8" rx="3" ry="6.5" fill="none" stroke="var(--sky)" stroke-width="1.1"/><line x1="1.5" y1="8" x2="14.5" y2="8" stroke="var(--sky)" stroke-width="1.1"/></svg>
        www.maplethorneek.com
      </p>
    </div>

    <div class="person">
      <p class="person__name">Rowan Ashby</p>
      <p class="person__title">President</p>
    </div>
  </section>

</body>
</html>
```